Business Card

I need a business card that really pops for a potential customer or person who refers a personal injury lead. I want to highlight our office locations, but only address that needs to be on the card is my office's main address. I want a sleek, modern and minimalist design.

```html
<!DOCTYPE html>
<html lang="en">
<head>
<meta charset="utf-8">
<title>Westline Injury Lawyers — Business Card</title>
<link href="https://fonts.googleapis.com/css2?family=Mulish:wght@300;400&display=swap" rel="stylesheet">
<style>
  :root {
    --backdrop: #1d1d1d;
    --card-dark: #3a3a3a;
    --card-light: #ffffff;
    --ink-dark: #2b2b2b;
    --ink-soft: #6b6b6b;
    --ink-light: #ffffff;
    --rule: #8a8a8a;
  }
  * { margin: 0; padding: 0; box-sizing: border-box; }
  html, body {
    width: 1200px;
    height: 875px;
    overflow: hidden;
    background: var(--backdrop);
    font-family: "Mulish", "Helvetica Neue", Arial, sans-serif;
    font-weight: 300;
  }
  .canvas {
    position: relative;
    width: 1200px;
    height: 875px;
  }
  .card {
    position: absolute;
    top: 288px;
    width: 525px;
    height: 300px;
    box-shadow: 0 18px 40px rgba(0,0,0,0.45);
  }
  .card--front { left: 50px; background: var(--card-dark); }
  .card--back  { left: 625px; background: var(--card-light); }

  .firm-name {
    position: absolute;
    left: 0; right: 0;
    text-align: center;
    font-weight: 400;
    letter-spacing: 0;
    line-height: 1.2;
    white-space: nowrap;
  }
  .card--front .firm-name { top: 128px; font-size: 34px; color: var(--ink-light); }
  .card--back  .firm-name { top: 80px;  font-size: 28px; color: var(--ink-dark); }

  .details {
    position: absolute;
    top: 168px;
    left: 0; right: 0;
    display: flex;
    justify-content: center;
    align-items: stretch;
  }
  .person {
    text-align: right;
    padding-right: 14px;
    padding-top: 22px;
    color: var(--ink-soft);
    font-size: 12.5px;
    line-height: 1.3;
  }
  .person__name {
    color: var(--ink-dark);
    font-size: 17px;
    text-transform: uppercase;
    letter-spacing: 0.02em;
    line-height: 1.1;
  }
  .person__role { margin-bottom: 6px; }
  .divider { width: 1px; background: var(--rule); }
  .contact {
    list-style: none;
    padding-left: 12px;
    color: var(--ink-soft);
    font-size: 12.5px;
    line-height: 1.6;
  }
  .contact li { display: flex; align-items: center; gap: 6px; }
  .contact svg { width: 10px; height: 10px; fill: var(--ink-dark); flex: none; }
</style>
</head>
<body>
<main class="canvas">
  <section class="card card--front" aria-label="Card front">
    <div class="firm-name">Westline Injury Lawyers</div>
  </section>

  <section class="card card--back" aria-label="Card back">
    <div class="firm-name">Westline Injury Lawyers</div>
    <div class="details">
      <div class="person">
        <div class="person__name">Daniel Reyes</div>
        <div class="person__role">Injury Lawyer</div>
        <div>4870 Alder Lane, Ste 02</div>
        <div>Marion, OH 43302</div>
      </div>
      <div class="divider"></div>
      <ul class="contact">
        <li>
          <svg viewBox="0 0 10 10" aria-hidden="true"><path d="M2 0.5 L3.6 0.5 L4.2 2.8 L3 3.6 Q4 5.8 6.4 7 L7.2 5.8 L9.5 6.4 L9.5 8 Q9.5 9.5 8 9.5 Q0.5 9 0.5 2 Q0.5 0.5 2 0.5Z"/></svg>
          555.210.4417
        </li>
        <li>
          <svg viewBox="0 0 10 10" aria-hidden="true"><path d="M2.5 0 H7.5 Q8.2 0 8.2 0.7 V9.3 Q8.2 10 7.5 10 H2.5 Q1.8 10 1.8 9.3 V0.7 Q1.8 0 2.5 0Z M2.8 1.2 V7.8 H7.2 V1.2Z"/></svg>
          555.318.2096
        </li>
        <li>
          <svg viewBox="0 0 10 10" aria-hidden="true"><path d="M0 1.8 H10 V8.2 H0Z" /><path d="M0.5 2.2 L5 5.6 L9.5 2.2" stroke="#fff" stroke-width="0.9" fill="none"/></svg>
          info@westlineinjurylaw.com
        </li>
        <li>
          <svg viewBox="0 0 10 10" aria-hidden="true"><circle cx="5" cy="5" r="4.6"/><path d="M0.6 5 H9.4 M5 0.4 Q2.6 5 5 9.6 M5 0.4 Q7.4 5 5 9.6" stroke="#fff" stroke-width="0.7" fill="none"/></svg>
          westlineinjurylaw.com
        </li>
      </ul>
    </div>
  </section>
</main>
</body>
</html>
```